Harbor Stone Legal, PLLC
There are several individuals who are reviewing these designs.
velmoranti: #1 is very good - high on the list. #2 - no to the vertical business card, horizontal is better. #4 is unique - I don't think all parties have seen it. Like that creativity though.
@bluquartzpen - the blue/gold color combo is too harsh. The logo is unique, but again, to severe.
@moxelarts - the same as above: the blue/gold combo is too severe looking.
@tenorubi - we do not like the red with blue/white combo and there seems to be a lot going on there.
Thanks to all who are participating!I hope this feedback helps.
Could you provide feedback for the designs that have been submitted to this point? Thanks!
I not sue why this is saying its on hold because it shouldn't be. Please submit.
This company does not have a logo.
@Pardo - we do not have a logo! That's part of this whole design gig here, isn't it?
Please upload ai or eps file of your logo.

```html
<!DOCTYPE html>
<html lang="en">
<head>
<meta charset="utf-8">
<title>Harbor Stone Legal, PLLC – Business Card</title>
<link rel="stylesheet" href="https://fonts.googleapis.com/css2?family=Lora:wght@400&family=Open+Sans:wght@400;700&display=swap">
<style>
  :root {
    --page: #ffffff;
    --card-front: #f6f6f6;
    --card-back: #e3e3e3;
    --card-edge: #d4d4d4;
    --ink: #1c1c1c;
    --ink-soft: #3a3a3a;
    --brand-blue: #1e6db5;
    --band-gray: #b9b9b9;
  }
  * { margin: 0; padding: 0; box-sizing: border-box; }
  html, body {
    width: 1200px; height: 398px; overflow: hidden;
    background: var(--page);
  }
  .canvas { position: relative; width: 1200px; height: 398px; }
  .card {
    position: absolute; top: 67px; width: 564px; height: 305px;
    border: 1px solid var(--card-edge);
    box-shadow: 0 2px 4px rgba(0,0,0,0.12);
  }
  .card--front { left: 19px; background: var(--card-front); }
  .card--back {
    left: 617px;
    background: linear-gradient(180deg, #e8e8e8 0%, var(--card-back) 100%);
  }
  .firm-name {
    font-family: "Lora", Georgia, serif;
    font-weight: 400; color: var(--ink); white-space: nowrap;
  }
  .card--front .firm-name {
    position: absolute; left: 22px; top: 12px; font-size: 27px; line-height: 34px;
  }
  .accent-bands { position: absolute; left: 0; top: 48px; }
  .divider {
    position: absolute; left: 240px; top: 96px;
    width: 2px; height: 190px; background: var(--brand-blue);
  }
  .contact {
    position: absolute; right: 16px; top: 98px;
    font-family: "Open Sans", Arial, sans-serif;
    font-size: 13.5px; line-height: 17.6px;
    color: var(--ink-soft); text-align: right; list-style: none;
  }
  .holder {
    position: absolute; left: 20px; top: 218px;
    font-family: "Open Sans", Arial, sans-serif; color: var(--ink);
  }
  .holder__name { font-size: 17px; font-weight: 700; line-height: 22px; }
  .holder__title { font-size: 14px; line-height: 20px; color: var(--ink-soft); }
  .card--back .firm-name {
    position: absolute; left: 0; right: 0; top: 130px;
    text-align: center; font-size: 31px; line-height: 40px;
  }
</style>
</head>
<body>
<div class="canvas">
  <section class="card card--front" aria-label="Card front">
    <h1 class="firm-name">Harbor Stone Legal, PLLC</h1>
    <svg class="accent-bands" width="564" height="30" viewBox="0 0 564 30" aria-hidden="true">
      <polygon points="0,2 112,2 96,22 0,22" fill="var(--band-gray)"/>
      <polygon points="116,6 564,6 564,28 98,28" fill="var(--brand-blue)"/>
    </svg>
    <div class="divider"></div>
    <ul class="contact">
      <li>2480 Linden Avenue</li>
      <li>Brookfield, Ohio 44403</li>
      <li>Toll free: English 330.555.0149</li>
      <li>Phone: Spanish 330.555.0294</li>
      <li>Cell: Vietnamese 330.555.0327</li>
      <li>Fax: 330.555.0460</li>
      <li>Email: meere@harborstonelegalpllc.com</li>
      <li>http://harborstonelegalpllc.com</li>
    </ul>
    <div class="holder">
      <p class="holder__name">R. Dalton Meere</p>
      <p class="holder__title">Attorney at Law</p>
    </div>
  </section>
  <section class="card card--back" aria-label="Card back">
    <p class="firm-name">Harbor Stone Legal, PLLC</p>
  </section>
</div>
</body>
</html>
```